American cannabis tech company business card design

Thrum.com is seeking a modern, professional, and brand-aligned business card that represents our company and its core values: Mission, Story, Values, and Impact. As an innovative cannabis company, we want a business card that is not only visually appealing but also serves as a representation of who we are and what we stand for.

Project Scope: Design a double-sided business card that integrates our brand identity and core values. Incorporate our key brand elements, ensuring a sleek and contemporary aesthetic. Visually reflect our core values (Mission, Story, Values, Impact) in a way that is engaging yet professional.

Target Market(s)

Vendors, third parties,

Contact Information for Business Card

Contact details (name, title, email, phone, website, etc.)

Font styles to use
Other font styles liked:
• Caslon, Centra

Colors

Designer to choose colors to be used in the design.

Requirements
Must have
• Thrum.com logo and branding A creative yet clean way to integrate our core values (Mission, Story, Values, Impact) Modern typography and a well-structured layout
Nice to have
• forest green, grey, white, black
Should not have
• references to marijuana, leafs, plants, or related product

```html
<!DOCTYPE html>
<html lang="en">
<head>
<meta charset="utf-8">
<title>Thrum.com Business Card</title>
<link rel="stylesheet" href="https://fonts.googleapis.com/css2?family=Playfair+Display:wght@700;900&family=Montserrat:wght@400;500&display=swap">
<style>
  :root {
    --forest: #1e3b22;
    --paper: #ffffff;
    --ink: #1f1f1f;
    --rule: #9a9a9a;
    --backdrop: #2a2d31;
  }
  * { box-sizing: border-box; margin: 0; padding: 0; }
  html, body { width: 1200px; height: 900px; overflow: hidden; }
  body {
    background: var(--backdrop);
    position: relative;
    font-family: "Montserrat", sans-serif;
  }
  .card {
    position: absolute;
    left: 290px;
    width: 620px;
    height: 354px;
    background: var(--paper);
    overflow: hidden;
  }
  .card--front { top: 70px; }
  .card--back { top: 476px; }
  .accent-bar {
    position: absolute;
    width: 22px;
    background: var(--forest);
  }
  .accent-bar--top { left: 0; top: 0; height: 150px; }
  .accent-bar--bottom { right: 0; bottom: 0; height: 150px; }
  .wordmark {
    font-family: "Playfair Display", serif;
    font-weight: 900;
    color: var(--forest);
    letter-spacing: 2px;
    line-height: 1;
    white-space: nowrap;
  }
  .card--front .wordmark {
    position: absolute;
    left: 0; right: 0; top: 50%;
    transform: translateY(-50%);
    text-align: center;
    font-size: 118px;
  }
  .card--back .wordmark {
    position: absolute;
    left: 56px;
    top: 132px;
    width: 244px;
    font-size: 56px;
    letter-spacing: 1px;
  }
  .details {
    position: absolute;
    left: 318px;
    top: 108px;
    padding-left: 22px;
    border-left: 1.5px solid var(--rule);
    height: 168px;
  }
  .person-name {
    font-family: "Playfair Display", serif;
    font-weight: 700;
    font-size: 21px;
    color: var(--forest);
    line-height: 1.2;
  }
  .person-title {
    font-family: "Playfair Display", serif;
    font-weight: 700;
    font-size: 10px;
    color: var(--ink);
    margin-bottom: 12px;
  }
  .address {
    font-size: 13px;
    line-height: 1.3;
    color: var(--ink);
    margin-bottom: 8px;
  }
  .contact-list { list-style: none; }
  .contact-item {
    display: flex;
    align-items: center;
    gap: 8px;
    font-size: 13px;
    line-height: 1.5;
    color: var(--ink);
  }
  .contact-icon { width: 11px; height: 11px; flex: none; }
</style>
</head>
<body>
  <section class="card card--front" aria-label="Card front">
    <span class="accent-bar accent-bar--top"></span>
    <span class="accent-bar accent-bar--bottom"></span>
    <h1 class="wordmark">THRUM</h1>
  </section>

  <section class="card card--back" aria-label="Card back">
    <span class="accent-bar accent-bar--top"></span>
    <span class="accent-bar accent-bar--bottom"></span>
    <h2 class="wordmark">THRUM</h2>
    <div class="details">
      <p class="person-name">Dana Whitlow</p>
      <p class="person-title">Owner</p>
      <p class="address">418 Cedar Park Ave, #112<br>Lakewood, OH 43210</p>
      <ul class="contact-list">
        <li class="contact-item">
          <svg class="contact-icon" viewBox="0 0 12 12"><path fill="#1e3b22" d="M2.5 0.8 4.3 0.5 5.3 3 4 4.1c.7 1.5 1.9 2.7 3.4 3.4L8.5 6.2 11 7.2 10.7 9c-.1.7-.7 1.2-1.4 1.1C5 9.7 1.9 6.5 1.4 2.2 1.3 1.5 1.8.9 2.5.8Z"/></svg>
          555-310-2284
        </li>
        <li class="contact-item">
          <svg class="contact-icon" viewBox="0 0 12 12"><rect x="0.5" y="2" width="11" height="8" rx="1" fill="#1e3b22"/><path d="M1 2.8 6 6.6 11 2.8" fill="none" stroke="#fff" stroke-width="1"/></svg>
          info@thrum.com
        </li>
        <li class="contact-item">
          <svg class="contact-icon" viewBox="0 0 12 12"><circle cx="6" cy="6" r="5.2" fill="none" stroke="#1e3b22" stroke-width="1.2"/><ellipse cx="6" cy="6" rx="2.2" ry="5.2" fill="none" stroke="#1e3b22" stroke-width="1"/><path d="M0.8 6h10.4" stroke="#1e3b22" stroke-width="1"/></svg>
          www.thrum.com
        </li>
      </ul>
    </div>
  </section>
</body>
</html>
```